Membership Based Medical Practice Website

We need a functioning website for a new Membership based medical practice. There will be an enrollment fee and a monthly fee. We would like to see designs that are modern, simple. Should use neutral light colors. Examples of sites we like are www.tallowbrookclinic.com and https://medicnearquill.com/ We also have a link that when "Join Now" is clicked it will go to the signup website.

Target Market(s)

Gay Men, local population, Age group 20 to 60's.

Industry/Entity Type

Medical

Coding

Coded - Design and coding required

Number of Pages Required

5+ page

Font styles to use
Sans Serif

Colors
ffffff
cee9f5
ecf7fb
cfeae6
edf8f6
aaaaaa
e9e9e9
dbdbdb
fff3d1

Requirements
Must have
• Logo and header on every page. Clean, simple design, clear content, mobile compatible.
• Must use Wordpress
Nice to have
• Ideas should come from tallowbrookclinic.com
• Easy to read
Should not have
• Generic patient pictures, bold colors.
• Should not copy from above websites.

```html
<!DOCTYPE html>
<html lang="en">
<head>
<meta charset="utf-8">
<title>Westbrook Infectious Disease Specialists</title>
<link href="https://fonts.googleapis.com/css2?family=Poppins:wght@300;400;500;600&family=Open+Sans:wght@400;600;700&family=Montserrat:wght@500;600&display=swap" rel="stylesheet">
<style>
:root{
  --white:#ffffff;
  --sky:#cee9f5;
  --sky-soft:#dcf0f8;
  --mist:#ecf7fb;
  --mint:#cfeae6;
  --grey:#aaaaaa;
  --line:#e9e9e9;
  --border:#dbdbdb;
  --ink:#1c1c1c;
  --text:#3a3a3a;
  --muted:#6b6b6b;
  --tick:#9fd3e4;
  --gold:#c9ad72;
  --night:#050505;
  --panel:#fafafa;
}
*{margin:0;padding:0;box-sizing:border-box}
html,body{width:1200px;height:2995px;overflow:hidden}
body{position:relative;background:var(--white);font-family:"Poppins",sans-serif;color:var(--text)}

/* header */
.site-header{position:absolute;top:0;left:0;width:1200px;height:130px;z-index:3;background:linear-gradient(#fff 0,#fff 60%,rgba(255,255,255,0) 100%)}
.brand{position:absolute;left:114px;top:10px;width:200px;text-align:center}
.brand-mark{display:block;margin:0 auto 8px;width:56px;height:56px;border:2px solid var(--gold);border-radius:50%}
.brand-name{font-family:"Montserrat",sans-serif;font-weight:500;color:#7c7c7c;font-size:12px;letter-spacing:9px;line-height:15px;white-space:nowrap}
.brand-sub{font-family:"Montserrat",sans-serif;font-weight:500;color:#7c7c7c;font-size:9.5px;line-height:12px;white-space:nowrap}
.main-nav{position:absolute;top:56px;left:488px;display:flex;align-items:center;font-family:"Montserrat",sans-serif;font-size:13.5px;color:#333;white-space:nowrap}
.main-nav a{text-decoration:none;color:inherit;margin-right:27px}
.main-nav a.current{font-weight:600;color:#111}
.join-btn{display:inline-block;background:var(--sky);border-radius:20px;padding:8px 23px;font-weight:600;color:#111;margin-right:0!important}

/* hero */
.hero{position:absolute;top:0;left:0;width:1200px;height:658px;background:linear-gradient(180deg,#f2f2f2 0%,#e4e6e4 28%,#b9bdb6 48%,#7f8a6c 66%,#4f5d44 82%,#3d4037 100%)}
.hero-title{position:absolute;top:240px;left:0;width:1200px;text-align:center;font-family:"Montserrat",sans-serif;font-weight:600;font-size:35px;line-height:58px;color:#9a9a9a;z-index:2}
.hero-notch{position:absolute;top:657px;left:588px;width:0;height:0;border-left:12px solid transparent;border-right:12px solid transparent;border-top:14px solid #3b3d38}

/* expertise */
.expertise{position:absolute;top:658px;left:0;width:1200px;height:586px;background:linear-gradient(90deg,#fff 0%,#fafafa 60%,#ededed 100%)}
.expertise-photo{position:absolute;right:0;top:40px;width:320px;height:546px;background:radial-gradient(ellipse at 60% 30%,#e6e6e6 0%,#cfcfcf 45%,#a9a9a9 100%);border-radius:160px 0 0 0}
.expertise h2{position:absolute;left:130px;top:88px;font-family:"Montserrat",sans-serif;font-weight:600;font-size:29px;color:var(--ink)}
.expertise .lead{position:absolute;left:132px;top:140px;font-size:15px;line-height:30px;color:#222}
.condition{position:absolute;display:flex;align-items:center;font-size:16.5px;color:#222;white-space:nowrap}
.condition svg{margin-right:20px}

/* benefits */
.benefits{position:absolute;top:1244px;left:0;width:1200px;height:876px;background:var(--panel)}
.benefits .kicker{position:absolute;top:88px;width:1200px;text-align:center;font-family:"Open Sans",sans-serif;font-size:13px;color:#333}
.benefits h2{position:absolute;top:124px;width:1200px;text-align:center;font-family:"Montserrat",sans-serif;font-weight:600;font-size:30px;color:var(--ink)}
.card{position:absolute;width:222px;height:258px;background:var(--white);border:1px solid var(--line);text-align:center;font-family:"Open Sans",sans-serif}
.card.is-active{background:var(--sky-soft);border-color:var(--sky-soft);box-shadow:0 2px 6px rgba(0,0,0,.08)}
.card svg{position:absolute;top:22px;left:75px}
.card h3{position:absolute;top:118px;left:0;width:100%;font-size:14.5px;font-weight:600;color:#222}
.card p{position:absolute;top:146px;left:14px;right:14px;font-size:12.5px;line-height:25px;color:#6a6a6a}
.card .more{position:absolute;display:block;top:206px;left:0;width:100%;text-align:center;font-size:13px;font-weight:700;color:#555;letter-spacing:.8px;text-decoration:underline;text-underline-offset:4px}

/* pricing */
.pricing-photo{position:absolute;left:130px;top:2206px;width:412px;height:372px;background:linear-gradient(180deg,#d9d2d6 0%,#e9c7a4 45%,#e0944b 70%,#8a5a33 100%)}
.pricing h2{position:absolute;left:586px;top:2192px;font-family:"Montserrat",sans-serif;font-weight:600;font-size:29px;color:var(--ink)}
.pricing .copy{position:absolute;left:588px;top:2242px;font-size:13.5px;line-height:30px;color:#222}
.perk{position:absolute;left:594px;display:flex;font-size:13.5px;line-height:36px;color:#222;white-space:nowrap}
.perk svg{margin:12px 18px 0 0;flex:none}
.learn-btn{position:absolute;left:588px;top:2548px;width:216px;height:46px;border-radius:23px;background:var(--sky);font-family:"Montserrat",sans-serif;font-weight:600;font-size:14px;color:#222;text-align:center;line-height:46px}

/* footer */
.site-footer{position:absolute;top:2672px;left:0;width:1200px;height:323px;background:var(--night);color:var(--white)}
.site-footer .brand{left:144px;top:34px}
.site-footer .brand-name,.site-footer .brand-sub{color:var(--white)}
.site-footer .brand-mark{border-color:var(--white)}
.footer-rule{position:absolute;left:426px;top:44px;width:1px;height:92px;background:#888}
.footer-note{position:absolute;left:500px;top:44px;width:560px;font-family:"Open Sans",sans-serif;font-size:15.5px;line-height:31px;color:var(--white)}
.footer-hr{position:absolute;left:100px;top:174px;width:992px;height:1px;background:#333}
.social{position:absolute;top:200px;left:432px;display:flex;gap:12px}
.social span{display:block;width:58px;height:58px;border:1px solid #777;border-radius:50%}
.copyright{position:absolute;top:288px;width:1200px;text-align:center;font-family:"Open Sans",sans-serif;font-size:11px;color:#ddd}
</style>
</head>
<body>

<header class="site-header">
  <div class="brand">
    <span class="brand-mark"></span>
    <div class="brand-name">WESTBROOK</div>
    <div class="brand-sub">INFECTIOUS DISEASE SPECIALISTS</div>
  </div>
  <nav class="main-nav">
    <a class="current">HOME</a><a>SPECIALTIES</a><a>PRICING</a><a>ABOUT US</a><a>FAQ</a><a>BLOG</a><a class="join-btn">JOIN US</a>
  </nav>
</header>

<section class="hero" role="img" aria-label="Misty country road running between green hills with sheep grazing beside it">
  <h1 class="hero-title">Specialty medicine with Commitment,<br>Compassion and Care</h1>
</section>
<div class="hero-notch"></div>

<section class="expertise">
  <div class="expertise-photo" role="img" aria-label="Black and white photo of a smiling woman in a scarf looking up"></div>
  <h2>WESTBROOK INFECTIOUS DISEASE specialists</h2>
  <p class="lead">We offer comprehensive treatment of a wide variety of infectious diseases.<br>Out expertise is in the following area.</p>

  <div class="condition" style="left:132px;top:258px"><svg width="14" height="14" viewBox="0 0 14 14"><circle cx="7" cy="7" r="6" fill="none" stroke="var(--tick)" stroke-width="1.3"/><path d="M4.3 7.2l1.9 1.8 3.5-3.6" fill="none" stroke="var(--tick)" stroke-width="1.3"/></svg>Tuberculosis</div>
  <div class="condition" style="left:132px;top:310px"><svg width="14" height="14" viewBox="0 0 14 14"><circle cx="7" cy="7" r="6" fill="none" stroke="var(--tick)" stroke-width="1.3"/><path d="M4.3 7.2l1.9 1.8 3.5-3.6" fill="none" stroke="var(--tick)" stroke-width="1.3"/></svg>Chronic Hepatitis</div>
  <div class="condition" style="left:132px;top:362px"><svg width="14" height="14" viewBox="0 0 14 14"><circle cx="7" cy="7" r="6" fill="none" stroke="var(--tick)" stroke-width="1.3"/><path d="M4.3 7.2l1.9 1.8 3.5-3.6" fill="none" stroke="var(--tick)" stroke-width="1.3"/></svg>Postsurgical infections</div>
  <div class="condition" style="left:132px;top:414px"><svg width="14" height="14" viewBox="0 0 14 14"><circle cx="7" cy="7" r="6" fill="none" stroke="var(--tick)" stroke-width="1.3"/><path d="M4.3 7.2l1.9 1.8 3.5-3.6" fill="none" stroke="var(--tick)" stroke-width="1.3"/></svg>Pre-travel vaccinations and counselling</div>
  <div class="condition" style="left:132px;top:466px"><svg width="14" height="14" viewBox="0 0 14 14"><circle cx="7" cy="7" r="6" fill="none" stroke="var(--tick)" stroke-width="1.3"/><path d="M4.3 7.2l1.9 1.8 3.5-3.6" fill="none" stroke="var(--tick)" stroke-width="1.3"/></svg>Infections associated with medical devices</div>
  <div class="condition" style="left:568px;top:258px"><svg width="14" height="14" viewBox="0 0 14 14"><circle cx="7" cy="7" r="6" fill="none" stroke="var(--tick)" stroke-width="1.3"/><path d="M4.3 7.2l1.9 1.8 3.5-3.6" fill="none" stroke="var(--tick)" stroke-width="1.3"/></svg>HIV/PrEP</div>
  <div class="condition" style="left:568px;top:310px"><svg width="14" height="14" viewBox="0 0 14 14"><circle cx="7" cy="7" r="6" fill="none" stroke="var(--tick)" stroke-width="1.3"/><path d="M4.3 7.2l1.9 1.8 3.5-3.6" fill="none" stroke="var(--tick)" stroke-width="1.3"/></svg>Bone and Joint infections</div>
  <div class="condition" style="left:568px;top:362px"><svg width="14" height="14" viewBox="0 0 14 14"><circle cx="7" cy="7" r="6" fill="none" stroke="var(--tick)" stroke-width="1.3"/><path d="M4.3 7.2l1.9 1.8 3.5-3.6" fill="none" stroke="var(--tick)" stroke-width="1.3"/></svg>Diabetes related infections</div>
  <div class="condition" style="left:568px;top:414px"><svg width="14" height="14" viewBox="0 0 14 14"><circle cx="7" cy="7" r="6" fill="none" stroke="var(--tick)" stroke-width="1.3"/><path d="M4.3 7.2l1.9 1.8 3.5-3.6" fill="none" stroke="var(--tick)" stroke-width="1.3"/></svg>Sexually transmitted infections</div>
</section>

<section class="benefits">
  <p class="kicker">We are not your traditional doctor's office.</p>
  <h2>LESS WAIT, MORE PERSONAL.</h2>

  <div class="card" style="left:128px;top:230px">
    <svg width="72" height="72" viewBox="0 0 72 72" fill="none" stroke="#666" stroke-width="2"><rect x="6" y="12" width="60" height="40" rx="2"/><path d="M28 52v8h16v-8M22 62h28"/><circle cx="36" cy="31" r="10"/><circle cx="36" cy="31" r="4"/></svg>
    <h3>Available when you are</h3>
    <p>New patient appointments are available within 1 week.</p>
    <span class="more">READ MORE</span>
  </div>
  <div class="card is-active" style="left:370px;top:230px">
    <svg width="72" height="72" viewBox="0 0 72 72" fill="none" stroke="#666" stroke-width="2"><path d="M14 60h44M22 60v-6h28v6M30 54l8-26M40 14l10 6-8 14-10-6z"/><circle cx="30" cy="42" r="6"/></svg>
    <h3>Save on lab costs</h3>
    <p>we offer discounted pricing of up to 90% off</p>
    <span class="more">READ MORE</span>
  </div>
  <div class="card" style="left:610px;top:230px">
    <svg width="72" height="72" viewBox="0 0 72 72" fill="none" stroke="#666" stroke-width="2"><path d="M36 44s-14-8-14-17a7 7 0 0 1 14-2 7 7 0 0 1 14 2c0 9-14 17-14 17z"/><path d="M6 46l12-6 14 8M66 26l-12 6-14-8"/></svg>
    <h3>Devoted care</h3>
    <p>We schedule enough time at each visit</p>
    <span class="more">READ MORE</span>
  </div>
  <div class="card" style="left:852px;top:230px">
    <svg width="72" height="72" viewBox="0 0 72 72" fill="none" stroke="#666" stroke-width="2"><rect x="8" y="20" width="42" height="24" rx="2"/><rect x="14" y="26" width="42" height="24" rx="2"/><ellipse cx="56" cy="44" rx="9" ry="3"/><path d="M47 44v14c0 2 18 2 18 0V44M47 50c0 2 18 2 18 0"/></svg>
    <h3>Straightforward pricing</h3>
    <p>We charge all our patients the same low rate - no surprises.</p>
    <span class="more">READ MORE</span>
  </div>

  <div class="card" style="left:128px;top:516px">
    <svg width="72" height="72" viewBox="0 0 72 72" fill="none" stroke="#666" stroke-width="2"><rect x="10" y="10" width="52" height="38" rx="2"/><path d="M30 48v8h12v-8M24 58h24"/><rect x="24" y="18" width="24" height="22"/><path d="M24 24h24M30 30h2M38 30h2M30 35h2M38 35h2"/></svg>
    <h3>Hassle-free booking</h3>
    <p>Schedule your appointment at your convenience</p>
    <span class="more">READ MORE</span>
  </div>
  <div class="card" style="left:370px;top:516px">
    <svg width="72" height="72" viewBox="0 0 72 72" fill="none" stroke="#666" stroke-width="2"><rect x="16" y="8" width="24" height="8"/><rect x="12" y="16" width="32" height="44" rx="3"/><path d="M28 30v12M22 36h12"/><rect x="38" y="46" width="26" height="12" rx="6" transform="rotate(-30 51 52)"/></svg>
    <h3>Save on medications</h3>
    <p>We offer deeply discounted wholesale price medications</p>
    <span class="more">READ MORE</span>
  </div>
  <div class="card" style="left:610px;top:516px">
    <svg width="72" height="72" viewBox="0 0 72 72" fill="none" stroke="#666" stroke-width="2"><rect x="14" y="8" width="38" height="54" rx="2"/><path d="M22 20h22M22 28h22M22 36h16M22 44h12M58 18L42 52l-4 2 1-4 16-34z"/></svg>
    <h3>Within your reach</h3>
    <p>Follow-up appointments &amp; video chat for your convenience.</p>
    <span class="more">READ MORE</span>
  </div>
  <div class="card" style="left:852px;top:516px">
    <svg width="72" height="72" viewBox="0 0 72 72" fill="none" stroke="#666" stroke-width="2"><rect x="8" y="18" width="42" height="32" rx="2"/><path d="M22 18v-6h14v6M26 30v8M22 34h8"/><circle cx="54" cy="44" r="6"/><path d="M42 62c0-8 6-10 12-10s12 2 12 10"/></svg>
    <h3>No middle man</h3>
    <p>We don't bill any insurance plans...</p>
    <span class="more">READ MORE</span>
  </div>
</section>

<section class="pricing">
  <div class="pricing-photo" role="img" aria-label="Four friends with arms around each other watching a golden sunset"></div>
  <h2>OUR PRICING</h2>
  <p class="copy">Our pricing is simple, transparent and affordable.<br>Membership Plan $80/mo, plus a one-time $99 enrollment fee.</p>
  <div class="perk" style="top:2318px"><svg width="14" height="12" viewBox="0 0 14 12"><path d="M1 6l4 4 8-9" fill="none" stroke="var(--tick)" stroke-width="2"/></svg>Includes all appointments, no co-pay</div>
  <div class="perk" style="top:2354px"><svg width="14" height="12" viewBox="0 0 14 12"><path d="M1 6l4 4 8-9" fill="none" stroke="var(--tick)" stroke-width="2"/></svg>Relaxed, unrushed visits</div>
  <div class="perk" style="top:2390px"><svg width="14" height="12" viewBox="0 0 14 12"><path d="M1 6l4 4 8-9" fill="none" stroke="var(--tick)" stroke-width="2"/></svg><span>Direct communication with your doctor via phone, email,<br>video chat 24/7</span></div>
  <div class="perk" style="top:2462px"><svg width="14" height="12" viewBox="0 0 14 12"><path d="M1 6l4 4 8-9" fill="none" stroke="var(--tick)" stroke-width="2"/></svg>Convenient online scheduling (no need to call during business hours)</div>
  <div class="perk" style="top:2498px"><svg width="14" height="12" viewBox="0 0 14 12"><path d="M1 6l4 4 8-9" fill="none" stroke="var(--tick)" stroke-width="2"/></svg>Wholesale price for labs and medications</div>
  <a class="learn-btn">LEARN MORE ABOUT US</a>
</section>

<footer class="site-footer">
  <div class="brand">
    <span class="brand-mark"></span>
    <div class="brand-name">WESTBROOK</div>
    <div class="brand-sub">INFECTIOUS DISEASE SPECIALISTS</div>
  </div>
  <div class="footer-rule"></div>
  <p class="footer-note">If you have any questions about our services before booking your appointment, please don't hesitate to email us at info@westbrookid.com or call us at 555-201-4477.</p>
  <div class="footer-hr"></div>
  <div class="social" aria-label="Social media links"><span></span><span></span><span></span><span></span><span></span></div>
  <p class="copyright">© Copyrights 2019 .All Rights Reserved.</p>
</footer>

</body>
</html>
```